【 概要 】 新発売する「ペルー産温州みかん」のパッケージデザインを募集します。 【 依頼内容 】 ・商品名:ペルー産温州みかん ・サイズ:W190×H225mm、GZ(底部分)40mm ・印刷範囲:全面印刷可能 ・素材の用意(画像・文章等):イラスト、写真等はお任せします。 文言は添付(文言.PDF)のPOPに入れる言葉を引用してもいいですし、 みかんに合うコピーを考えていただいてもいいです。 ・デザイン内容:スーパーで売られる予定の商品で、売り場で映える洗練されたデザイン 【 デザインイメージ 】 ・ターゲット層:20〜40代女性 ・雰囲気:みかんのリアルなイラストや写真を入れて、高級感がありおしゃれなイメージ ・参考デザイン: 参考1~3の画像 【 契約金額(税込み) 】 19,800円 ※契約金額(税込)からシステム利用料を差し引いた金額が、ワーカーさまの受取金額となります その他ご質問等ありましたら、気軽にお問い合わせください。 ご応募をお待ちしております! |
どの提案も素敵でしたが、今回はこちらの案を採用させていただきます。
温州みかんのイラストの雰囲気がよく、商品名とシズルのイメージのバランスがよかったです。
皆さま、今回たくさんの提案いただきありがとうございました。
どの案もすばらしかったため、選定するのに時間がかかってしまいました。
弊社では、またこのようなパッケージデザインの依頼をさせていただくことがあります。
ぜひ、またご提案いただけたらと思います。
今回はありがとうございました。

```html
<!DOCTYPE html>
<html lang="ja">
<head>
<meta charset="UTF-8">
<title>温州みかん パッケージ</title>
<link href="https://fonts.googleapis.com/css2?family=Shippori+Mincho:wght@400;500&family=Noto+Sans+JP:wght@400&family=Parisienne&display=swap" rel="stylesheet">
<style>
  :root {
    --paper: #ffffff;
    --outline: #9a9a9a;
    --gusset: #f1f1f1;
    --ink: #4a4a4a;
    --ink-soft: #5c5c5c;
    --orange: #ef8a2a;
    --orange-light: #f9b25a;
    --orange-deep: #e07818;
  }
  html, body {
    margin: 0;
    padding: 0;
    overflow: hidden;
    background: var(--paper);
  }
  .canvas {
    position: relative;
    width: 1032px;
    height: 1200px;
    overflow: hidden;
    background: var(--paper);
  }
  .dieline {
    position: absolute;
    inset: 0;
  }
  .fruit-art, .origin-map {
    position: absolute;
  }
  .fruit-art {
    left: 125px;
    top: 615px;
    width: 500px;
    height: 300px;
    border-radius: 50%;
    background: radial-gradient(ellipse at 42% 38%, var(--orange-light) 0%, var(--orange) 60%, var(--orange-deep) 100%);
  }
  .origin-map {
    left: 472px;
    top: 240px;
    width: 44px;
    height: 50px;
    border-radius: 40% 30% 45% 35%;
    background: var(--orange);
  }
  .origin-line {
    position: absolute;
    left: 0;
    width: 1032px;
    top: 296px;
    margin: 0;
    text-align: center;
    font-family: "Shippori Mincho", serif;
    font-size: 29px;
    letter-spacing: 1px;
    color: var(--ink);
  }
  .product-name {
    position: absolute;
    left: 0;
    width: 1032px;
    top: 378px;
    margin: 0;
    text-align: center;
    font-family: "Shippori Mincho", serif;
    font-weight: 400;
    font-size: 90px;
    letter-spacing: 10px;
    color: var(--ink);
  }
  .latin-name {
    position: absolute;
    left: 0;
    width: 1032px;
    top: 508px;
    margin: 0;
    text-align: center;
    font-family: "Parisienne", cursive;
    font-size: 36px;
    letter-spacing: 4px;
    color: var(--ink-soft);
  }
  .story {
    position: absolute;
    left: 630px;
    top: 650px;
    margin: 0;
    font-family: "Noto Sans JP", sans-serif;
    font-size: 18.5px;
    line-height: 36px;
    color: var(--ink);
  }
</style>
</head>
<body>
<div class="canvas">
  <svg class="dieline" width="1032" height="1200" viewBox="0 0 1032 1200">
    <defs>
      <radialGradient id="leafGlow" cx="50%" cy="50%" r="50%">
        <stop offset="0%" stop-color="#8cc55a" stop-opacity="0.85"/>
        <stop offset="55%" stop-color="#c6e4a2" stop-opacity="0.6"/>
        <stop offset="100%" stop-color="#eef7e2" stop-opacity="0"/>
      </radialGradient>
      <clipPath id="panelClip">
        <rect x="59" y="59" width="914" height="968"/>
      </clipPath>
    </defs>
    <polygon class="gusset" points="59,1027 973,1027 920,1093 920,1173 112,1173 112,1093"
             fill="var(--gusset)" stroke="var(--outline)" stroke-width="2"/>
    <rect class="front-panel" x="59" y="59" width="914" height="968" fill="var(--paper)"/>
    <g class="leaf-art" role="img" aria-label="新緑の葉のイラスト" clip-path="url(#panelClip)">
      <ellipse cx="170" cy="150" rx="330" ry="230" fill="url(#leafGlow)"/>
      <ellipse cx="900" cy="130" rx="260" ry="170" fill="url(#leafGlow)"/>
      <ellipse cx="880" cy="830" rx="280" ry="330" fill="url(#leafGlow)"/>
      <ellipse cx="130" cy="980" rx="200" ry="110" fill="url(#leafGlow)"/>
    </g>
    <rect x="59" y="59" width="914" height="968" fill="none" stroke="var(--outline)" stroke-width="2"/>
    <rect class="handle-hole" x="427" y="120" width="173" height="67" rx="33"
          fill="var(--paper)" stroke="var(--outline)" stroke-width="2"/>
  </svg>

  <div class="fruit-art" role="img" aria-label="葉付きの温州みかん二個のイラスト"></div>
  <div class="origin-map" role="img" aria-label="ペルーの地図"></div>

  <p class="origin-line">南米大陸ペルー共和国生まれ</p>
  <h1 class="product-name">温州みかん</h1>
  <p class="latin-name">Citrus Unshiu</p>

  <p class="story">今から約80年前に日本移民が<br>栽培したのが始まりです。<br>アンデス山脈から出ずる豊かな水と<br>南太平洋から降り注ぐ<br>太陽の光を浴びて育んだ<br>まろやかで美味しいみかんです。</p>
</div>
</body>
</html>
```